Vollo Activewear business card design

I need a business card designed for my activewear business. I would like to use the colours pink, purple white and blue. please see attached logo. please include (name) Rosalind Thwaite (phone) 0417285630 (email) rozzivollo@mailbrook.net (ABN) 51837264019 . please include - Free shipping on all orders over $100

Target Market(s)

female

Contact Information for Business Card

Colors

Designer to choose colors to be used in the design.

Requirements
Must have
• I need a business card designed for my activewear business. I would like to use the colours pink, purple white and blue. please see attached logo. please include (name) Rosalind Thwaite (phone) 0417285630 (email) rozzivollo@mailbrook.net (ABN) 51837264019 . please include - Free shipping on all orders over $100

```html
<!DOCTYPE html>
<html lang="en">
<head>
<meta charset="utf-8">
<title>Vollo Activewear – Business Card</title>
<link rel="stylesheet" href="https://fonts.googleapis.com/css2?family=Lato:wght@400;700;900&display=swap">
<style>
  :root {
    --stage: #e6e4e8;
    --purple: #9c1aab;
    --purple-deep: #8a1598;
    --paper: #ffffff;
    --ink: #1d1d1f;
    --white: #ffffff;
  }
  * { box-sizing: border-box; margin: 0; padding: 0; }
  html, body {
    width: 1200px; height: 912px; overflow: hidden;
    background: var(--stage);
    font-family: "Lato", sans-serif;
  }
  .sheet {
    position: relative; width: 1200px; height: 912px;
    display: flex; flex-direction: column; align-items: center; justify-content: center; gap: 44px;
  }
  .card {
    position: relative; width: 630px; height: 360px;
    box-shadow: 0 10px 26px rgba(0,0,0,0.22);
    overflow: hidden;
  }
  /* Front */
  .card--front { background: var(--purple); color: var(--white); }
  .front__brand {
    position: absolute; left: 0; right: 0; top: 96px;
    text-align: center; font-weight: 900; font-size: 104px; letter-spacing: 6px;
    line-height: 1;
  }
  .front__offer {
    position: absolute; left: 0; right: 0; bottom: 58px;
    text-align: center; font-weight: 700; font-size: 19px; letter-spacing: 0.5px;
    text-transform: uppercase;
  }
  /* Back */
  .card--back { background: var(--paper); }
  .back__brand {
    position: absolute; left: 48px; top: 160px;
    display: flex; align-items: center; gap: 14px;
  }
  .back__dot { width: 26px; height: 26px; border-radius: 50%; background: var(--purple); }
  .back__name-mark {
    font-weight: 900; font-size: 44px; letter-spacing: 3px; color: var(--purple); line-height: 1;
  }
  .back__divider {
    position: absolute; left: 310px; top: 96px; width: 2px; height: 150px; background: var(--purple);
  }
  .contact {
    position: absolute; left: 340px; top: 98px; color: var(--ink);
    font-size: 16px; line-height: 1.55;
  }
  .contact__name { color: var(--purple); font-weight: 700; font-size: 25px; margin-bottom: 8px; }
  .contact__row { display: flex; align-items: center; gap: 10px; }
  .contact__icon { width: 14px; height: 14px; flex: none; fill: var(--purple); }
  .contact__row--plain { padding-left: 0; }
</style>
</head>
<body>
<main class="sheet">
  <section class="card card--front" aria-label="Card front">
    <div class="front__brand">VOLLO</div>
    <p class="front__offer">Free shipping on all orders over $100</p>
  </section>

  <section class="card card--back" aria-label="Card back">
    <div class="back__brand">
      <span class="back__dot"></span>
      <span class="back__name-mark">VOLLO</span>
    </div>
    <div class="back__divider"></div>
    <div class="contact">
      <p class="contact__name">Rosalind Thwaite</p>
      <p class="contact__row contact__row--plain">(ABN) 51837264019</p>
      <p class="contact__row">
        <svg class="contact__icon" viewBox="0 0 24 24" aria-hidden="true"><path d="M6.6 10.8a15.1 15.1 0 0 0 6.6 6.6l2.2-2.2c.3-.3.7-.4 1-.2 1.1.4 2.3.6 3.6.6.6 0 1 .4 1 1V20c0 .6-.4 1-1 1A17 17 0 0 1 3 4c0-.6.4-1 1-1h3.5c.6 0 1 .4 1 1 0 1.3.2 2.5.6 3.6.1.3 0 .7-.2 1l-2.3 2.2z"/></svg>
        0417285630
      </p>
      <p class="contact__row">
        <svg class="contact__icon" viewBox="0 0 24 24" aria-hidden="true"><path d="M2 5h20v14H2z" opacity=".35"/><path d="M2 5l10 8 10-8v2l-10 8L2 7z"/></svg>
        rozzivollo@mailbrook.net
      </p>
    </div>
  </section>
</main>
</body>
</html>
```